Electronic Music Artist needs an Album Cover

DRELL is an electronic musician from Boston, Massachusetts. He needs an album cover that captures the essence of his music. The album is called Waypoints, which represents his experiences growing up, positive and negative. He would like to see designs that involves color and creativity. Attached are some examples of artworks that DRELL likes. He also included a few of his original photos (optional to use. Using a photo will not effect his final decision!), and his logo.
Updates

Colors

Designer to choose colors to be used in the design.

Requirements
Must have
• My project must have the text "Waypoints" and "DRELL", and the logo (attached in the files). The logo should not be the main subject of the artwork. Everything must look aesthetically pleasing.
Nice to have
• It would be nice to have some sort of creative graphic design (see example album covers for reference). Also, in one of the references, there is a column on the left hand side with some text in it. That could be cool to include, but without the asian text.
Should not have
• The project should not have any other language besides English.

```html
<!DOCTYPE html>
<html lang="en">
<head>
<meta charset="utf-8">
<title>DRELL — Waypoints</title>
<link rel="stylesheet" href="https://fonts.googleapis.com/css2?family=Michroma&family=Jura:wght@300&display=swap">
<style>
  :root {
    --ink-cyan: #6ee6e4;
    --ink-white: #f2eef0;
    --sky-red: #c8262e;
    --sky-deep: #5a0f1c;
    --fog-lilac: #a89ac4;
    --fog-pale: #c9bfdc;
    --band-shade: rgba(30, 7, 16, 0.45);
  }
  * { margin: 0; padding: 0; box-sizing: border-box; }
  html, body { width: 1200px; height: 1200px; overflow: hidden; background: #1a0d14; }
  .cover { position: relative; width: 1200px; height: 1200px; overflow: hidden; }
  .cover-photo {
    position: absolute; inset: 0;
    background:
      radial-gradient(ellipse 60% 40% at 15% 55%, rgba(240,140,80,0.85), transparent 70%),
      radial-gradient(ellipse 55% 30% at 80% 60%, rgba(225,50,60,0.8), transparent 70%),
      linear-gradient(180deg, var(--sky-deep) 0%, #8e1a2a 22%, var(--sky-red) 45%, #b8485a 62%, #7d6a9a 78%, var(--fog-lilac) 88%, var(--fog-pale) 100%);
  }
  .geometry { position: absolute; inset: 0; width: 1200px; height: 1200px; }
  .artist-name {
    position: absolute; top: 62px; left: 0; width: 1200px;
    text-align: center;
    font-family: "Michroma", sans-serif; font-weight: 400;
    font-size: 100px; line-height: 1;
    letter-spacing: 50px; padding-left: 50px;
    color: var(--ink-cyan);
  }
  .album-title-row {
    position: absolute; top: 712px; left: 0; width: 1200px;
    display: flex; justify-content: center;
  }
  .album-title {
    display: inline-block;
    padding: 10px 24px 10px 50px;
    background: var(--band-shade);
    font-family: "Jura", sans-serif; font-weight: 300;
    font-size: 44px; line-height: 1;
    letter-spacing: 26px;
    color: var(--ink-white);
  }
</style>
</head>
<body>
  <main class="cover">
    <div class="cover-photo" role="img" aria-label="Photo collage of upward-looking city towers blended into a red sunset sky over misty mountain ridges and fog"></div>

    <svg class="geometry" viewBox="0 0 1200 1200" aria-hidden="true">
      <circle class="orbit-fill" cx="600" cy="520" r="290" fill="#2a0610" opacity="0.3"/>
      <circle class="orbit-ring" cx="600" cy="520" r="330" fill="none" stroke="#6ee6e4" stroke-width="2" opacity="0.45"/>
      <circle class="orbit-ring-inner" cx="600" cy="520" r="230" fill="none" stroke="#f2eef0" stroke-width="1" opacity="0.3"/>
      <polygon class="slash-orange" points="150,1000 330,1000 690,180 510,180" fill="#f08a2a" opacity="0.35"/>
      <polygon class="slash-crimson" points="620,1000 700,1000 1060,180 980,180" fill="#b3122e" opacity="0.5"/>
      <line class="horizon-rule" x1="120" y1="880" x2="1080" y2="880" stroke="#f2eef0" stroke-width="1" opacity="0.4"/>
    </svg>

    <h1 class="artist-name">DRELL</h1>
    <div class="album-title-row">
      <h2 class="album-title">WAYPOINTS</h2>
    </div>
  </main>
</body>
</html>
```